Tech Laundry service company looking for a new modern and clean web site

Our site is www.brisklinenhub.com we are looking to rebrand our whole website.

We offer free pickup and delivery for laundry and dry cleaning in the NYC area. we target residential customers.

Sites to compare are www.trypolvex.com and www.zentumo.com
Most content can be found at www.brisklinenhub.com

We are looking for a clean and modern look. Nothing to busy

colors and font we use are
Logo font: Harabara
Slogan font: Swiss 721 Light Extended BT

Dark blue: C 100 M 88 Y 0 K 0
Light blue: C 85 M 50 Y 0 K 0
Orange: C 0 M 80 Y 95 K 0

Violet: C 85 M 100 Y 0 K 0

We use only Marlo, Quilse and vendrax
We are provide eco-friendly
next day laundry service

Our mission Statement is to deliver the Cleanest and Brightest clothes in the market. we use only top of the line

"We are the #1 proud supporter of Marlo and Quilse"

There will be 4 pages
the home page
and a 2 page scheduling page

THE HOME PAGE-
navigation bar must include

Home,
Clean my Clothes (schedule a pickup)
Pricing
Blog
Service Area
Commercial/Wholesale
Sign in
must have key elements about our business such as:
1. Our Price is 1.10 a lb
2. "New customers get 50% off first order and 100% off second order!"
3. we have next day service on all laundry orders
Again, you can pull the content off our current website brisklinenhub.com

Order Page-

Attached please find 5 steps of the ordering page. We are looking to condense into 2
we want step2+step3+step4 on one page
then step1+step5 on the second page on step5 we want the coinbird logo attached as well (as we do all credit card processing through CoinBird)
at the end of the process we want to offer them to create a password to auto register
the order confirmation is attached as well. we need all that info but would like it to seem cleaner and modern.

PRICING PAGE-

Wash and Fold 1.10 per Lb ($27 min charge)
Blankets $12 and up
Bathroom Rugs $5.00 and up

Dry Cleaning
Launder and Press shirt 1.25
Suit Jacket 6.00
Pants and Skirts 6.00
2 pc suit 12.00
Dress 10.00 and up
Blouses & Sweaters 6.00

Again, we are looking for a clean and sleek site not to busy.

Based on this we will be needed another 6-8 pages of design work that will be negotiated with the winner at the end of this contest.
Good Luck!

Target Market(s)

our customers are between the ages of 22-40 years old all live in NYC

Industry/Entity Type

Dry Cleaning

Number of Pages Required

4 page

Font styles to use
Other font styles liked:
• Harabara

Requirements
Must have
• sleek and cool design
• see www.polvex.com and zentumo.com for concept
• Our current site is brisklinenhub.com which we are looking to rebrand
Nice to have
• colors and font we use are
• Logo font: Harabara
• Slogan font: Swiss 721 Light Extended BT
• Dark blue: C 100 M 88 Y 0 K 0
• Light blue: C 85 M 50 Y 0 K 0
• Orange: C 0 M 80 Y 95 K 0
• Violet: C 85 M 100 Y 0 K 0
Should not have
• we want all the colors to be uniform. we are sending a message that we are the brightest and cleanest laundry service in the city!

```html
<!DOCTYPE html>
<html lang="en">
<head>
<meta charset="utf-8">
<title>Brisk Linen Hub — NYC Laundry Delivery</title>
<link href="https://fonts.googleapis.com/css2?family=Lato:wght@300;400;700&display=swap" rel="stylesheet">
<style>
:root{
  --dark-blue:#1d4a9c;
  --light-blue:#1e62b8;
  --orange:#e8482b;
  --orange-light:#f2865a;
  --violet:#3d1b8c;
  --text:#333;
  --muted:#555;
  --footer-bg:#f2f2f2;
  --white:#fff;
}
*{box-sizing:border-box;margin:0;padding:0}
html,body{width:1200px;height:2500px;overflow:hidden}
body{font-family:'Lato',sans-serif;color:var(--text);background:var(--white);position:relative}
.block{position:absolute;left:0;width:1200px}

/* header */
.site-header{top:0;height:87px;background:var(--white)}
.brand{position:absolute;left:112px;top:24px;display:flex;align-items:center;gap:8px}
.brand-dot{width:36px;height:36px;border-radius:50%;background:var(--light-blue)}
.brand-name{font-size:22px;font-weight:700;color:var(--orange)}
.main-nav a{position:absolute;top:32px;font-size:13.5px;line-height:16px;color:var(--dark-blue);text-decoration:none;white-space:nowrap}
.sign-in{position:absolute;left:1005px;top:27px;width:83px;height:30px;background:var(--orange);color:var(--white);font-size:15px;display:flex;align-items:center;justify-content:center}

/* hero */
.hero{top:87px;height:455px;background:linear-gradient(100deg,#1a54a8 0%,#1e62b8 45%,#2a6cc2 70%,#1a58ae 100%)}
.hero-title{position:absolute;left:137px;top:168px;font-size:34px;font-weight:400;color:var(--white);line-height:44px}
.btn{display:flex;align-items:center;justify-content:center;color:var(--white);font-size:15px;position:absolute;white-space:nowrap}
.hero-btn{left:137px;top:281px;width:125px;height:35px;background:var(--orange)}
.hero-dots{position:absolute;left:137px;top:346px;display:flex;gap:4px}
.hero-dots span{width:7px;height:7px;border-radius:50%;background:var(--white)}
.hero-dots span.active{background:var(--orange)}

/* how it works */
.how{top:542px;height:421px}
.section-title{position:absolute;left:0;width:1200px;text-align:center;font-weight:400}
.how .section-title{top:65px;font-size:30px;color:#222}
.step{position:absolute;top:133px;width:330px;text-align:center}
.step svg{width:74px;height:74px}
.step-title{margin-top:46px;font-size:16px;color:var(--dark-blue);font-weight:400}
.step-text{margin-top:18px;font-size:13px;line-height:22px;color:var(--muted)}

/* join band */
.join{top:963px;height:352px;background:radial-gradient(ellipse at 50% 45%,var(--orange-light) 0%,#ee6a3f 40%,var(--orange) 80%)}
.join .section-title{top:97px;font-size:30px;color:var(--white)}
.join-text{position:absolute;left:115px;width:970px;top:162px;text-align:center;color:var(--white);font-size:13px;line-height:22px}
.join-btn{left:538px;top:255px;width:124px;height:35px;background:var(--light-blue)}

/* customers */
.customers{top:1315px;height:148px}
.customers .section-title{top:22px;font-size:15px;color:#222;letter-spacing:.5px}
.customer-list{position:absolute;top:80px;left:0;width:1200px;display:flex;justify-content:center;gap:60px;align-items:center}
.customer-list span{font-size:20px;font-weight:700;color:var(--dark-blue)}

/* schedule band */
.schedule{top:1463px;height:352px;background:linear-gradient(120deg,#32157a 0%,var(--violet) 40%,#4a22a0 70%,#2e1370 100%)}
.schedule .section-title{top:124px;font-size:30px;color:var(--white)}
.schedule-btn{left:493px;top:189px;width:215px;height:34px;background:var(--orange)}

/* content */
.content{top:1815px;height:405px}
.info{position:absolute;top:98px;width:300px}
.info h3{font-size:20px;font-weight:400;color:var(--orange);line-height:22px}
.info p{margin-top:18px;font-size:11.5px;line-height:20px;color:#333}
.testimonial{position:absolute;left:780px;top:77px;width:308px;height:275px;background:var(--light-blue);color:var(--white);padding:32px 18px}
.testimonial h4{font-size:20px;font-weight:400}
.quote-mark{font-size:60px;line-height:40px;margin-top:20px;font-style:italic;font-weight:300}
.testimonial blockquote{font-size:19px;font-weight:300;line-height:28px;margin-top:6px}
.testimonial cite{display:block;font-style:normal;font-size:19px;margin-top:8px}

/* footer */
.site-footer{top:2220px;height:233px;background:var(--footer-bg)}
.foot-col{position:absolute;top:40px}
.foot-col h5{font-size:15px;font-weight:400;color:var(--dark-blue);margin-bottom:22px}
.foot-col li{list-style:none;font-size:12px;line-height:22px;color:#222}
.foot-col p{font-size:12px;line-height:22px;color:#222}
.bottom-bar{top:2453px;height:47px;text-align:center;font-size:11.5px;line-height:47px;color:#222}
</style>
</head>
<body>

<header class="block site-header">
  <div class="brand"><span class="brand-dot"></span><span class="brand-name">Brisk Linen Hub</span></div>
  <nav class="main-nav">
    <a href="#" style="left:445px">Home</a>
    <a href="#" style="left:508px">Clean My Clothes</a>
    <a href="#" style="left:635px">Pricing</a>
    <a href="#" style="left:702px">Blog</a>
    <a href="#" style="left:755px">Service Area</a>
    <a href="#" style="left:855px">Commercial/Wholesale</a>
  </nav>
  <a class="sign-in">Sign in</a>
</header>

<section class="block hero" role="img" aria-label="Photo of a man in a checked shirt beside a white front-loading washing machine, tinted blue">
  <h1 class="hero-title">We are the #1 proud supporter of<br>Marlo, Vendrax and Quilse</h1>
  <a class="btn hero-btn">Learn More</a>
  <div class="hero-dots"><span class="active"></span><span></span><span></span><span></span></div>
</section>

<section class="block how">
  <h2 class="section-title">How It Works</h2>
  <div class="step" style="left:53px">
    <svg viewBox="0 0 74 74"><circle cx="37" cy="37" r="30" fill="none" stroke="#e8482b" stroke-width="5"/><path d="M37 20v18l10 6" fill="none" stroke="#e8482b" stroke-width="5" stroke-linecap="round"/><path d="M6 52c4 10 12 16 18 16l6-8-8-6-5 4c-3-2-5-5-6-9z" fill="#e8482b"/></svg>
    <h3 class="step-title">Next Day Delivery</h3>
    <p class="step-text">Astonishing fast service, ready in 24 hours from pickup<br>time, delivered to your doorsteps.</p>
  </div>
  <div class="step" style="left:435px">
    <svg viewBox="0 0 74 74"><rect x="18" y="6" width="42" height="56" rx="3" fill="#e8482b" transform="rotate(14 39 34)"/><g stroke="#fff" stroke-width="3"><line x1="28" y1="22" x2="52" y2="28"/><line x1="26" y1="31" x2="50" y2="37"/><line x1="24" y1="40" x2="48" y2="46"/></g><path d="M10 52l14 14" stroke="#e8482b" stroke-width="6" stroke-linecap="round"/></svg>
    <h3 class="step-title">Free Pickup &amp; Delivery</h3>
    <p class="step-text">We mean it, everything included in the same price, our<br>drivers are out in the city from 9AM to 7PM.</p>
  </div>
  <div class="step" style="left:768px">
    <svg viewBox="0 0 74 74"><path d="M37 6l30 14v34L37 68 7 54V20z" fill="#e8482b"/><path d="M7 20l30 14 30-14M37 34v34" fill="none" stroke="#fff" stroke-width="2"/><path d="M44 54V44l-3 3M50 54V44l3 3" fill="none" stroke="#fff" stroke-width="2"/></svg>
    <h3 class="step-title">Only $1.10 a Pound?</h3>
    <p class="step-text">Yes and that also includes high quality, on time service<br>and great customer service, we believe its time to<br>make a difference.</p>
  </div>
</section>

<section class="block join">
  <h2 class="section-title">Join Thousands of Satisfied New Yorkers</h2>
  <p class="join-text">Brisk Linen Hub is NYC Laundry Delivery service at its best. Founded in 2008, our business has expanded to six locations and serves all of Manhattan! We offer free laundry delivery service for a set price of $1.10 per pound for residential and commercial customers. We also offer dry-cleaning services at great prices. You can call or schedule a pickup online and we'll pick it up the same day. You won't find a laundry delivery service that's better than that!</p>
  <a class="btn join-btn">LEARN MORE</a>
</section>

<section class="block customers">
  <h2 class="section-title">OUR CUSTOMER</h2>
  <div class="customer-list"><span>Peakcast</span><span>Aerolane</span><span>Gridleague</span><span>Voltway</span><span>Big Top Troupe</span></div>
</section>

<section class="block schedule" role="img" aria-label="Soft-focus photo of laundry, tinted violet">
  <h2 class="section-title">Clean My Clothes</h2>
  <a class="btn schedule-btn">SCHEDULE A PICK UP</a>
</section>

<section class="block content">
  <article class="info" style="left:110px">
    <h3>A Customized Commercial<br>Laundry Service</h3>
    <p>Our superior commercial laundry service is available for hotels, restaurants and a whole range of commercial customers. Among our past clients are Peakcast, Aerolane, Gridleague, Voltway and Big Top Troupe. Your laundry will be custom washed according to your preferences as well as professionally folded. All of our laundry is checked for quality assurance so that your business can maintain its high standards. If you're looking for a quality hotel or restaurant laundry service, come to Brisk Linen Hub!</p>
  </article>
  <article class="info" style="left:445px">
    <h3>Laundry Pickup and Delivery<br>7 Days a Week</h3>
    <p>Our superior commercial laundry service is available for hotels, restaurants and a whole range of commercial customers. Among our past clients are Peakcast, Aerolane, Gridleague, Voltway and Big Top Troupe. Your laundry will be custom washed according to your preferences as well as professionally folded. All of our laundry is checked for quality assurance so that your business can maintain its high standards. If you're looking for a quality hotel or restaurant laundry service, come to Brisk Linen Hub!</p>
  </article>
  <aside class="testimonial">
    <h4>Testimonials</h4>
    <div class="quote-mark">“</div>
    <blockquote>The detergent that you guys use smells so good!, I've gotten complements on the smell!</blockquote>
    <cite>Dana - Manhattan</cite>
  </aside>
</section>

<footer class="block site-footer">
  <div class="foot-col" style="left:115px">
    <h5>Quick Links</h5>
    <ul><li>Home</li><li>Clean my Clothes</li><li>Pricing</li><li>Blog</li><li>Service Area</li><li>Commercial/Wholesale</li></ul>
  </div>
  <div class="foot-col" style="left:338px">
    <h5>Contact Us</h5>
    <p>Brisk Linen Hub</p><p>&nbsp;</p>
    <p>(212) 555-0148</p><p>48 Harbor Lane, NY, NY, 10004, USA</p><p>orders@brisklinenhub.com</p>
  </div>
  <div class="foot-col" style="left:550px">
    <h5>Convenient Laundry Service</h5>
    <ul><li>24 Hour Turnaround.</li><li>Free Pickup and Delivery</li><li>Easy Online Access.</li></ul>
  </div>
  <div class="foot-col" style="left:782px;width:310px">
    <h5 style="margin-bottom:4px">Peace of Mind</h5>
    <p>Quality Assurance.</p><p>&nbsp;</p>
    <p>Every piece of laundry is handle with care by our trained attendants, we guarantee our service by double checking you wont have any missing clothes before delivery.</p>
  </div>
</footer>

<div class="block bottom-bar">Brisk Linen Hub LLC © 2013 | Terms of Service | Privacy Policy</div>

</body>
</html>
```